Blast Off -

I need to launch a new website that more accurately reflects what we do as a business. We are an IT Reseller that specialises in delivering innovative solutions covering supply, implementation and support. My current website is www.tervanbnr.com and was something I designed myself on the Web Wren website. This was fine for the first 2 years but now I need something more professional and detailed. A couple of websites for companies similar to Tervan BNR are www.dranvolt.co.uk and www.mirendaway.co.uk. By looking at these it will hopefully give you an idea as to what I am trying to achieve.

Target Market(s)

UK based companies with between 30-250 employees, no fixed vertical

Coding

Coded - Design and coding required

Number of Pages Required

4 page

Font styles to use
Sans Serif

Colors
33a6d7
0592cd
85cae6

Requirements
Must have
• Contact details page to include a "Get in touch with us " section, About Us page, IT Support page to include the headings 1/ Proactive Monitoring 2/ 24 x 7 Support 3/ Security and Data Back-up 4/ Built-in Compliance (GDPR) 5/ Responsive IT Support. I am happy to provide the wording for these headings.
Clean crisp home screen with a Menu offering the requested drop down options.
Nice to have
• Easy to navigate site with a good flow. I have updated a page regarding cloud services, this would be great to have as a separate drop down menu option. I would like to have different Cloud logo's in ideally the Tervan Blue colour. Can you please add the photograph of Penhorrow Hall which is my office in the contact us page.
Should not have
• I definitely DO NOT want a photo/view of London on the home page!!

```html
<!DOCTYPE html>
<html lang="en">
<head>
<meta charset="utf-8">
<title>Tervan BNR – IT Services</title>
<link href="https://fonts.googleapis.com/css2?family=Montserrat:ital,wght@0,300;0,400;0,500;0,600;0,700;0,800;0,900;1,300;1,400&family=Playfair+Display:wght@400&display=swap" rel="stylesheet">
<style>
:root{
  --blue:#00a7e6;
  --blue-dark:#0592cd;
  --blue-soft:#85cae6;
  --ink:#111111;
  --text:#333a40;
  --muted:#7a8088;
  --accent:#f2603f;
  --pink:#f0316a;
  --tint:#f0f6fa;
  --card-line:#f7dcd5;
  --white:#ffffff;
}
*{margin:0;padding:0;box-sizing:border-box}
html,body{width:1200px;height:4129px;overflow:hidden;background:var(--white)}
body{font-family:"Montserrat",sans-serif;color:var(--text);position:relative}
.abs{position:absolute}

/* top bar */
.topbar{top:0;left:0;width:1200px;height:42px;background:var(--blue);color:var(--white);font-size:8px}
.topbar .info{top:17px;left:160px;display:flex;gap:32px;align-items:center}
.topbar .info span{display:flex;align-items:center;gap:5px}
.topbar .social{top:14px;left:986px;display:flex;gap:4px}
.topbar .social i{width:14px;height:14px;border-radius:50%;background:var(--white);display:block}

/* header */
.header{top:42px;left:0;width:1200px;height:97px;background:var(--white)}
.brand{top:24px;left:165px;display:flex;align-items:center;gap:14px}
.brand-dot{width:66px;height:66px;border-radius:50%;background:var(--blue-dark)}
.brand-name{font-size:24px;font-weight:500;color:var(--ink)}
.nav{top:58px;left:623px;display:flex;font-size:14px;font-weight:500;color:var(--ink)}
.nav a{color:inherit;text-decoration:none;margin-right:48px;display:flex;align-items:center;gap:3px}
.nav a.active{color:var(--blue)}

/* hero */
.hero{top:139px;left:0;width:1200px;height:582px;background:linear-gradient(120deg,#7d858c 0%,#4e565c 45%,#3a4046 70%,#8a8f92 100%)}
.hero-text{width:1200px;text-align:center;color:var(--white)}
.hero-kicker{top:184px;font-size:36px;font-weight:400}
.hero-title{top:222px;font-size:102px;font-weight:900;letter-spacing:1px;line-height:1}
.hero-sub{top:318px;font-size:27px;font-weight:300;line-height:33px}

/* about */
.about{top:721px;left:0;width:1200px;height:650px;background:var(--tint);overflow:hidden}
.eyebrow{font-size:17px;font-weight:500;color:var(--blue);display:flex;align-items:center;gap:18px}
.dots{display:inline-block;width:82px;border-bottom:2px dotted var(--blue);height:0;margin-top:8px}
.about .eyebrow{top:191px;left:160px}
.about h2{top:222px;left:160px;font-size:31px;font-weight:800;color:var(--ink);line-height:36px;width:360px}
.about p{left:159px;width:320px;font-size:12px;line-height:15.6px;color:#222}
.about .p1{top:378px}
.about .p2{top:473px}
.btn{top:581px;left:160px;width:204px;height:52px;border-radius:26px;background:var(--blue);color:var(--white);font-size:17px;font-weight:500;display:flex;align-items:center;justify-content:center}
.about-circle{top:225px;left:590px;width:478px;height:478px;border-radius:50%;background:var(--blue)}
.about-photo{top:115px;left:622px;width:380px;height:535px;border-radius:190px 190px 0 0;background:linear-gradient(180deg,#e3c9b2 0%,#b69a86 40%,#8c8581 100%)}

/* services */
.section-label{width:1200px;justify-content:center}
.section-title{width:1200px;text-align:center;font-weight:800;color:var(--ink)}
.svc-label{top:1484px}
.svc-title{top:1515px;font-size:54px}
.card{width:231px;height:202px;border:2px solid var(--card-line);background:var(--white)}
.card .icon{top:30px;left:28px;width:34px;height:34px}
.card h3{top:30px;left:72px;font-size:16px;font-weight:700;color:var(--ink);line-height:19px;width:150px}
.card p{top:90px;left:30px;width:180px;font-size:9.4px;line-height:16px;color:#555}
.card .more{top:153px;left:34px;font-size:9px;font-weight:600;color:var(--ink);display:flex;align-items:center;gap:12px}
.card .more i{width:18px;height:18px;border-radius:50%;border:1px solid #f3c9bf;color:var(--accent);font-style:normal;font-size:10px;display:flex;align-items:center;justify-content:center}

/* cta */
.cta{top:2075px;left:0;width:1200px;height:210px;background:var(--blue);color:var(--white);text-align:center}
.cta .kicker{top:22px;width:1200px;font-size:31px;font-weight:300}
.cta h2{top:70px;width:1200px;font-size:47px;font-weight:800;line-height:56px}

/* team */
.team-label{top:2356px}
.team-title{top:2400px;font-size:42px}
.member{width:268px;height:390px}
.member .photo{top:0;left:0;width:268px;height:312px;background:linear-gradient(180deg,#d9dde0 0%,#b9a497 55%,#9a9ea3 100%)}
.member .info{top:284px;left:17px;width:233px;height:104px;background:var(--white);box-shadow:0 4px 14px rgba(0,0,0,.08)}
.member .info::before{content:"";position:absolute;left:0;top:40px;width:2px;height:16px;background:var(--accent)}
.member .role{top:20px;left:26px;font-size:8px;color:var(--blue-soft)}
.member .name{top:34px;left:26px;font-family:"Playfair Display",serif;font-size:19px;color:#444}
.member .socials{top:68px;left:26px;display:flex;gap:10px}
.member .socials i{width:9px;height:9px;border-radius:2px;background:#c8d0d6;display:block}
.member .badge{top:-12px;left:176px;width:36px;height:36px;border-radius:50%;background:var(--white);border:1px solid #f3d5cd;display:flex;align-items:center;justify-content:center}

/* testimonials */
.testi-label{top:2982px}
.testi-title{top:3012px;font-size:40px}
.tcard{width:220px;height:165px;border-radius:14px;background:#eef3f7}
.tcard .quote{top:-14px;left:18px;font-size:64px;font-weight:900;color:var(--blue);line-height:1;font-family:"Montserrat",sans-serif}
.tcard .stars{top:30px;left:20px;font-size:9px;color:#f5a623;letter-spacing:1px}
.tcard h4{top:48px;left:20px;font-size:11px;font-weight:700;color:var(--ink)}
.tcard p{top:70px;left:20px;width:182px;font-size:8.4px;line-height:16px;color:#555}
.author{display:flex;align-items:center;gap:14px}
.author .avatar{width:30px;height:30px;border-radius:50%;background:#7d8188}
.author b{display:block;font-size:10.5px;font-weight:600;color:var(--blue)}
.author span{font-size:8px;color:#444}
.pager{top:3396px;left:543px;display:flex;gap:6px}
.pager i{width:34px;height:4px;border-radius:2px;background:#d6dadd;display:block}
.pager i.on{background:var(--blue)}

/* newsletter */
.newsletter{top:3489px;left:0;width:1200px;height:213px;background:var(--blue)}
.newsletter h3{top:54px;width:1200px;text-align:center;font-size:23px;font-weight:300;font-style:italic;color:var(--white)}
.subscribe{top:96px;left:415px;width:368px;height:40px;border-radius:20px;background:var(--white)}
.subscribe .ph{top:14px;left:18px;font-size:9px;color:#9aa}
.subscribe .go{top:0;left:227px;width:141px;height:40px;border-radius:20px;background:var(--pink);color:var(--white);font-size:9px;font-weight:700;display:flex;align-items:center;justify-content:center}

/* footer */
.footer .brand{top:3738px}
.fhead{font-size:16px;font-weight:700;color:var(--blue);top:3826px}
.fabout{top:3862px;left:160px;width:350px;font-size:15.5px;line-height:19.2px;color:#222}
.flist{top:3861px;list-style:none;font-size:15.5px;line-height:22.4px;color:#222}
</style>
</head>
<body>

<div class="abs topbar">
  <div class="abs info">
    <span><svg width="9" height="9" viewBox="0 0 10 10"><path d="M1 6V5a4 4 0 0 1 8 0v1M1 6h2v3H1zM7 6h2v3H7z" fill="none" stroke="#fff" stroke-width="1.2"/></svg>+44 20 7946 0821</span>
    <span><svg width="10" height="8" viewBox="0 0 10 8"><rect x=".5" y=".5" width="9" height="7" fill="none" stroke="#fff"/><path d="M.5 .5l4.5 4 4.5-4" fill="none" stroke="#fff"/></svg>hello@tervanbnr.com</span>
    <span>Mon - Sat 9.00 - 18.00, Sunday</span>
  </div>
  <div class="abs social"><i></i><i></i><i></i></div>
</div>

<header class="abs header">
  <div class="abs brand"><div class="brand-dot"></div><div class="brand-name">Tervan BNR</div></div>
  <nav class="abs nav">
    <a class="active">Home</a>
    <a>IT Support <svg width="9" height="6" viewBox="0 0 9 6"><path d="M1 1l3.5 3.5L8 1" fill="none" stroke="#111" stroke-width="1.4"/></svg></a>
    <a>About Us</a>
    <a>Contact Us</a>
  </nav>
</header>

<section class="abs hero" role="img" aria-label="Photograph of a support technician with a headset working at a desktop computer in an office">
  <div class="abs hero-text hero-kicker">We Focus On</div>
  <div class="abs hero-text hero-title">IT SERVICES</div>
  <div class="abs hero-text hero-sub">specialises in delivering innovative solutions<br>covering supply, implementation and support</div>
</section>

<section class="abs about">
  <div class="abs eyebrow">ABOUT US <span class="dots"></span></div>
  <h2 class="abs">Innovative Solutions Covering Supply, Implementation and Support</h2>
  <p class="abs p1">Lorem ipsum dolor sit amet, consectetur adipiscing elit, sed do eiusmod tempor incididunt ut labore et dolore magna aliqua. Quis ipsum suspendisse ultrices gravida. Risus commodo viverra maecenas accumsan lacus vel facilisis.</p>
  <p class="abs p2">Lorem ipsum dolor sit amet, consectetur adipiscing elit, sed do eiusmod tempor incididunt ut labore et dolore magna aliqua. Quis ipsum suspendisse ultrices gravida. Risus commodo viverra maecenas accumsan lacus vel facilisis.</p>
  <div class="abs btn">READ MORE</div>
  <div class="abs about-circle"></div>
  <div class="abs about-photo" role="img" aria-label="Photograph of a smiling consultant in glasses and a checked blazer with arms crossed"></div>
</section>

<div class="abs eyebrow section-label svc-label"><span class="dots"></span>ABOUT US<span class="dots"></span></div>
<h2 class="abs section-title svc-title">What We Do</h2>

<div class="abs card" style="top:1613px;left:234px">
  <svg class="abs icon" viewBox="0 0 34 34" fill="none" stroke="#f2603f" stroke-width="1.6"><path d="M4 30h20M8 30l6-10 8-6M22 8l6 6M18 12l6-6"/><circle cx="14" cy="20" r="2"/></svg>
  <h3 class="abs">Proactive Monitoring</h3>
  <p class="abs">Lorem ipsum dolor sit amet, conse ctetur adipiscing elit, sed do eiusmod tempor incididunt ut labore et dolore.</p>
  <div class="abs more">Read More <i>+</i></div>
</div>
<div class="abs card" style="top:1613px;left:484px">
  <svg class="abs icon" viewBox="0 0 34 34" fill="none" stroke="#f2603f" stroke-width="1.6"><path d="M17 8a8 8 0 0 0-5 14v4h10v-4a8 8 0 0 0-5-14zM13 30h8M17 1v3M5 12H2M32 12h-3M8 4l2 2M26 4l-2 2"/></svg>
  <h3 class="abs">24 x 7<br>Suppor</h3>
  <p class="abs">Lorem ipsum dolor sit amet, conse ctetur adipiscing elit, sed do eiusmod tempor incididunt ut labore et dolore.</p>
  <div class="abs more">Read More <i>+</i></div>
</div>
<div class="abs card" style="top:1613px;left:734px">
  <svg class="abs icon" viewBox="0 0 34 34" fill="none" stroke="#f2603f" stroke-width="1.6"><path d="M17 2l13 7v14l-13 9-13-9V9z"/><path d="M11 17l4 4 8-8"/></svg>
  <h3 class="abs">Security and Data Back-up</h3>
  <p class="abs">Lorem ipsum dolor sit amet, conse ctetur adipiscing elit, sed do eiusmod tempor incididunt ut labore et dolore.</p>
  <div class="abs more">Read More <i>+</i></div>
</div>
<div class="abs card" style="top:1834px;left:234px">
  <svg class="abs icon" viewBox="0 0 34 34" fill="none" stroke="#f2603f" stroke-width="1.6" style="top:30px"><rect x="3" y="4" width="28" height="8" rx="1"/><rect x="3" y="14" width="28" height="8" rx="1"/><rect x="3" y="24" width="28" height="8" rx="1"/><path d="M7 8h8M7 18h8M7 28h8"/></svg>
  <h3 class="abs" style="top:16px">Built-in Compliance (GDPR)</h3>
  <p class="abs" style="top:84px">Lorem ipsum dolor sit amet, conse ctetur adipiscing elit, sed do eiusmod tempor incididunt ut labore et dolore.</p>
  <div class="abs more" style="top:150px">Read More <i>+</i></div>
</div>
<div class="abs card" style="top:1834px;left:484px">
  <svg class="abs icon" viewBox="0 0 34 34" fill="none" stroke="#f2603f" stroke-width="1.6"><path d="M17 32s11-11 11-19a11 11 0 0 0-22 0c0 8 11 19 11 19z"/><circle cx="17" cy="13" r="4"/></svg>
  <h3 class="abs">Responsive IT Support</h3>
  <p class="abs" style="top:84px">Lorem ipsum dolor sit amet, conse ctetur adipiscing elit, sed do eiusmod tempor incididunt ut labore et dolore.</p>
  <div class="abs more" style="top:150px">Read More <i>+</i></div>
</div>
<div class="abs card" style="top:1834px;left:734px">
  <svg class="abs icon" viewBox="0 0 34 34" fill="none" stroke="#f2603f" stroke-width="1.6"><path d="M3 10s6-7 14-7 14 7 14 7-6 7-14 7S3 10 3 10z"/><circle cx="17" cy="10" r="3"/><path d="M17 17v15M12 24h10M13 30h8"/></svg>
  <h3 class="abs">Responsive IT Support</h3>
  <p class="abs" style="top:84px">Lorem ipsum dolor sit amet, conse ctetur adipiscing elit, sed do eiusmod tempor incididunt ut labore et dolore.</p>
  <div class="abs more" style="top:150px">Read More <i>+</i></div>
</div>

<section class="abs cta">
  <div class="abs kicker">Ready to Take Action?</div>
  <h2 class="abs">Contact Us Today And<br>Get A FREE Quote</h2>
</section>

<div class="abs eyebrow section-label team-label"><span class="dots"></span>OUR TEM<span class="dots" style="margin-left:-18px"></span></div>
<h2 class="abs section-title team-title">Meet Our Professional Team</h2>

<div class="abs member" style="top:2528px;left:26px">
  <div class="abs photo" role="img" aria-label="Portrait photograph of the founder in a grey hoodie"></div>
  <div class="abs info">
    <div class="abs badge"><svg width="14" height="14" viewBox="0 0 14 14" fill="none" stroke="#f2603f" stroke-width="1.2"><path d="M1 6l12-5-5 12-2-5z"/></svg></div>
    <div class="abs role">Founder</div>
    <div class="abs name">Marisol T. Arden</div>
    <div class="abs socials"><i></i><i></i><i></i><i></i><i></i></div>
  </div>
</div>
<div class="abs member" style="top:2528px;left:319px">
  <div class="abs photo" role="img" aria-label="Portrait photograph of the chief executive in glasses"></div>
  <div class="abs info">
    <div class="abs badge"><svg width="14" height="14" viewBox="0 0 14 14" fill="none" stroke="#f2603f" stroke-width="1.2"><rect x="1" y="3" width="9" height="9"/><rect x="4" y="1" width="9" height="9"/></svg></div>
    <div class="abs role">CEO</div>
    <div class="abs name">Oriana P. Vesk</div>
    <div class="abs socials"><i></i><i style="background:#f2603f"></i><i></i><i></i><i></i></div>
  </div>
</div>
<div class="abs member" style="top:2528px;left:612px">
  <div class="abs photo" role="img" aria-label="Portrait photograph of the designer with curly hair"></div>
  <div class="abs info">
    <div class="abs badge"><svg width="14" height="14" viewBox="0 0 14 14" fill="none" stroke="#f2603f" stroke-width="1.2"><path d="M2 12l8-8M8 2l4 4"/></svg></div>
    <div class="abs role">Designer</div>
    <div class="abs name">Tobin R. Halvard</div>
    <div class="abs socials"><i></i><i></i><i></i><i></i><i></i></div>
  </div>
</div>
<div class="abs member" style="top:2528px;left:907px">
  <div class="abs photo" role="img" aria-label="Portrait photograph of the developer in a light blazer"></div>
  <div class="abs info">
    <div class="abs badge"><svg width="14" height="14" viewBox="0 0 14 14" fill="none" stroke="#f2603f" stroke-width="1.2"><path d="M7 2l6 3-6 3-6-3zM1 8l6 3 6-3"/></svg></div>
    <div class="abs role">Developer</div>
    <div class="abs name">Caspian J. Ordell</div>
    <div class="abs socials"><i></i><i></i><i></i><i></i><i></i></div>
  </div>
</div>

<div class="abs eyebrow section-label testi-label"><span class="dots"></span>TESTIMONILAS<span class="dots"></span></div>
<h2 class="abs section-title testi-title">More Than 500K Clients Loves Us</h2>

<div class="abs tcard" style="top:3140px;left:256px">
  <div class="abs quote">“</div>
  <div class="abs stars">★★★★★</div>
  <h4 class="abs">100% Recommended</h4>
  <p class="abs">Duis aute irure dolor in reprehenderit in voluptate velit esse cillum dolore eu fugiat nulla pariatur. eaque ipsa quae incididunt ut labore et dolore magna aliqua nulla pariatu cillum dolore eu.</p>
</div>
<div class="abs author" style="top:3335px;left:278px"><div class="avatar"></div><div><b>Ellis Marr</b><span>CEO, Abc Company</span></div></div>

<div class="abs tcard" style="top:3140px;left:493px">
  <div class="abs quote">“</div>
  <div class="abs stars">★★★★★</div>
  <h4 class="abs">They are the Best</h4>
  <p class="abs">Lorem ipsum dolor sit amet consectetur adipiscing elit, sed do eiusmod tempor incididunt ut labore et dolore magna aliqua. Duis aute irure dolor in reprehenderit in voluptate velit esse cillum dolore.</p>
</div>
<div class="abs author" style="top:3335px;left:516px"><div class="avatar"></div><div><b>Priya Lund</b><span>CEO, Abc Company</span></div></div>

<div class="abs tcard" style="top:3140px;left:732px">
  <div class="abs quote">“</div>
  <div class="abs stars">★★★★★</div>
  <h4 class="abs">Loved Their Work</h4>
  <p class="abs">Duis aute irure dolor in reprehenderit in voluptate velit esse cillum dolore eu fugiat nulla pariatur. eaque ipsa quae incididunt ut labore et dolore magna aliqua nulla pariatu cillum dolore eu.</p>
</div>
<div class="abs author" style="top:3335px;left:753px"><div class="avatar"></div><div><b>Solenne Ray</b><span>CEO, Abc Company</span></div></div>

<div class="abs pager"><i></i><i class="on"></i><i></i></div>

<section class="abs newsletter">
  <h3 class="abs">Subscribe To Our Newsletter</h3>
  <div class="abs subscribe">
    <div class="abs ph">Your Mail</div>
    <div class="abs go">Subscribe</div>
  </div>
</section>

<footer class="footer">
  <div class="abs brand"><div class="brand-dot"></div><div class="brand-name">Tervan BNR</div></div>
  <div class="abs fhead" style="left:160px">ABOUT US</div>
  <p class="abs fabout">Lorem ipsum dolor sit amet, consectetur adipiscing elit, sed do eiusmod tempor incididunt ut labore et dolore magna aliqua. Quis ipsum suspendisse ultrices gravida. Risus commodo viverra maecenas accumsan lacus vel facilisis.</p>
  <div class="abs fhead" style="left:559px">IT SERVICES</div>
  <ul class="abs flist" style="left:562px">
    <li>&nbsp;Proactive Monitoring</li>
    <li>24 x 7 Support</li>
    <li>Security and Data Back-up</li>
    <li>Built-in Compliance (GDPR)</li>
    <li>Responsive IT Suppor</li>
  </ul>
  <div class="abs fhead" style="left:809px">COMPANY</div>
  <ul class="abs flist" style="left:814px">
    <li>About Us</li>
    <li>Our Team</li>
    <li>Blog</li>
    <li>Contact Us</li>
    <li>Location</li>
  </ul>
</footer>

</body>
</html>
```